Clothing Brand E-Commerce Website Design

We would like you to provide an ecommerce design template in layered PSD for our clothing/fashion brand website called "FernQuill".
We want the site to have a simple but sleek design similar to the following sites:
http://www.threadorbit.example/
http://tovalenwick.example/
http://www.sadiplume.example/
We want it to look stunning and blow the example sites out of the water. For color scheme, please use your imagination and try to impress us with your creativity.
We like teal and beige pink, with teal dominant.
Teal #7AFFFF / #46C6C6
Beige/pink #FF7B7C / #C74646
We want you to develop the design for 3 pages:
1) Home Page
Samples:
http://www.threadorbit.example/
http://tovalenwick.example/
http://www.sadiplume.example/
2) Products List Page (e.g., lists all "Dresses" when category is selected)
http://www.threadorbit.example/shop/casual-dresses
http://www.sadiplume.example/index.php?main_page=index&cPath=3
http://tovalenwick.example/modest-dresses.html
http://www.lunahive88.example/Product/Category.aspx?br=lh8&category=dress_maxi
3) Product Detail Page (e.g., individual product page with "Add to Cart")
http://www.threadorbit.example/shop/dresses/willow-dawn-dress
http://tovalenwick.example/modest-dresses/modest-dress-opal.html
http://www.sadiplume.example/index.php?main_page=product_info&cPath=3&products_id=297
Industry/Entity Type
Fashion

```html
<!DOCTYPE html>
<html lang="en">
<head>
<meta charset="utf-8">
<title>FernQuill – It's your fashion brand</title>
<link href="https://fonts.googleapis.com/css2?family=Source+Sans+3:wght@400;600;700&display=swap" rel="stylesheet">
<style>
  :root {
    --teal: #46c6c6;
    --teal-light: #cde9e8;
    --teal-pale: #e6f4f3;
    --red: #c74646;
    --red-deep: #b3252c;
    --ink: #1c1c1c;
    --grey: #6e6e6e;
    --line: #b9c2c2;
    --black: #060304;
    --white: #ffffff;
    --footer-tag: #8c7b7b;
  }
  * { box-sizing: border-box; margin: 0; padding: 0; }
  html, body { width: 993px; height: 1200px; overflow: hidden; }
  body {
    position: relative;
    font-family: "Source Sans 3", "Helvetica Neue", Arial, sans-serif;
    color: var(--ink);
    background: #fbf8f4;
  }
  .abs { position: absolute; }

  /* top utility bar */
  .utility-bar { left: 0; top: 0; width: 993px; height: 20px; background: var(--teal); z-index: 3; }
  .utility-bar .join { left: 683px; top: 0; width: 41px; height: 20px; background: var(--red); color: var(--white); font-size: 10px; line-height: 20px; text-align: center; }
  .utility-bar .sign-in { left: 733px; top: 0; color: var(--white); font-size: 10px; line-height: 20px; }

  /* header */
  .site-header { left: 0; top: 20px; width: 993px; height: 48px; background: linear-gradient(#ffffff, #eceeee); border-bottom: 2px solid #e3d9d9; z-index: 3; }
  .brand { display: flex; align-items: center; gap: 5px; }
  .brand .mark { width: 22px; height: 22px; background: var(--teal); }
  .brand .name { font-size: 22px; font-weight: 400; color: var(--red); line-height: 1; }
  .tagline { font-size: 7.5px; line-height: 9px; color: #777; letter-spacing: .5px; margin-top: 1px; }
  .site-header .brand-wrap { left: 194px; top: 5px; }
  .site-header .divider { left: 331px; top: 10px; width: 1px; height: 28px; background: #d8dcdc; }
  .main-nav { left: 357px; top: 19px; display: flex; gap: 15px; font-size: 10px; color: var(--teal); }
  .main-nav .new { color: var(--red); }
  .search { left: 683px; top: 17px; width: 107px; height: 16px; background: var(--white); border: 1px solid #d6dada; }
  .search svg { position: absolute; right: 4px; top: 3px; }

  /* page backdrop */
  .backdrop { left: 0; top: 69px; width: 993px; height: 987px;
    background:
      radial-gradient(circle at 290px 170px, rgba(255,255,240,.95) 0, rgba(255,255,240,0) 260px),
      radial-gradient(circle at 40px 340px, rgba(255,255,255,.35) 0, rgba(255,255,255,0) 45px),
      radial-gradient(circle at 760px 340px, rgba(255,255,255,.3) 0, rgba(255,255,255,0) 50px),
      linear-gradient(#b9d3d0 0, #d7e4df 300px, #eef0ea 560px, #fbf7f2 800px, #fdfaf6 987px); }

  /* hero */
  .hero { left: 184px; top: 83px; width: 621px; height: 214px; overflow: hidden;
    background:
      radial-gradient(ellipse 140px 60px at 370px 150px, rgba(255,255,245,.95) 0, rgba(255,255,245,0) 100%),
      radial-gradient(ellipse 170px 190px at 150px 110px, rgba(244,236,232,.85) 0, rgba(244,236,232,0) 100%),
      linear-gradient(180deg, rgba(0,0,0,0) 0, rgba(0,0,0,0) 150px, rgba(90,150,165,.55) 165px, rgba(215,232,230,.9) 185px, rgba(225,215,200,.9) 214px),
      linear-gradient(90deg, #dfeaec 0%, #b4d2dc 35%, #7fb0c3 70%, #4f879f 100%);
    box-shadow: 0 12px 10px -8px rgba(0,0,0,.35); }
  .hero .cta { left: 363px; top: 165px; width: 126px; height: 25px; border-radius: 13px; background: var(--red-deep); color: var(--white); font-size: 11.5px; line-height: 25px; text-align: center; z-index: 2; font-family: Georgia, "Times New Roman", serif; }
  .slider-dots { left: 479px; top: 318px; display: flex; gap: 5px; }
  .slider-dots span { width: 11px; height: 11px; border-radius: 50%; background: var(--teal); border: 1.5px solid var(--white); }
  .slider-dots span.active { background: var(--red-deep); }

  /* featured product */
  .feature-card { left: 216px; top: 364px; width: 184px; height: 194px; background: #c9d5d3; }
  .feature-card .photo { left: 7px; top: 8px; width: 170px; height: 178px; background: linear-gradient(135deg, #f2b23b 0%, #e66b2b 45%, #d9d4cc 100%); }
  .feature-card .ribbon { left: 0; top: 0; width: 0; height: 0; border-top: 44px solid #f2c200; border-right: 44px solid transparent; }
  .feature-card .ribbon-text { left: 3px; top: 8px; transform: rotate(-45deg); font-size: 9px; color: #b7262c; font-weight: 600; }
  .feature-card .shop-bar { left: 13px; top: 160px; width: 157px; height: 24px; background: rgba(199,70,70,.85); color: var(--white); font-size: 11px; line-height: 24px; }
  .feature-card .shop-bar .label { left: 11px; }
  .feature-card .shop-bar .price { left: 93px; }
  .cart-btn { background: var(--teal); display: flex; align-items: center; justify-content: center; }
  .feature-card .cart-btn { left: 131px; top: 2px; width: 22px; height: 20px; }

  .welcome { left: 429px; top: 366px; width: 350px; }
  .welcome h1 { font-size: 21px; font-weight: 400; margin-bottom: 12px; }
  .welcome p { font-size: 8.8px; line-height: 11.3px; margin-bottom: 11px; }
  .btn-dark { background: var(--black); color: var(--white); border-radius: 7px; font-size: 8.5px; text-align: center; box-shadow: 0 6px 6px -3px rgba(0,0,0,.25); }
  .welcome .btn-dark { position: relative; width: 57px; height: 22px; line-height: 22px; margin-top: 8px; }

  /* product tabs */
  .tabs { left: 199px; top: 594px; display: flex; }
  .tabs .tab { width: 112px; height: 28px; line-height: 30px; text-align: center; font-size: 11px; background: var(--teal-pale); border-bottom: 3px solid var(--teal-light); }
  .tabs .tab.active { background: var(--teal-light); }
  .product-panel { left: 199px; top: 623px; width: 586px; height: 221px; background: var(--white); border: 1px solid var(--line); }
  .product { top: 17px; width: 116px; height: 156px; box-shadow: 0 8px 8px -6px rgba(0,0,0,.35); }
  .product.p1 { left: 17px; background: linear-gradient(#7e8a95, #a7a1c4); }
  .product.p2 { left: 163px; background: linear-gradient(#6f7780, #9a9fa4); }
  .product.p3 { left: 310px; background: linear-gradient(#6c6c70, #8d3a40); }
  .product.p4 { left: 450px; background: linear-gradient(#e9eef2, #7fa9cf); }
  .product .overlay { left: 0; top: 91px; width: 116px; height: 65px; background: rgba(170,50,60,.82); color: var(--white); font-size: 10.5px; line-height: 19px; padding: 4px 0 0 9px; }
  .product .overlay .cart-btn { left: 89px; top: 40px; width: 22px; height: 20px; }
  .product-panel .blurb { left: 17px; top: 185px; width: 450px; font-size: 8.8px; line-height: 11.3px; color: var(--grey); }
  .product-panel .btn-dark { left: 510px; top: 187px; width: 57px; height: 22px; line-height: 22px; }

  /* info columns */
  .info-col { top: 873px; width: 185px; }
  .info-col h2 { font-size: 18px; font-weight: 400; color: var(--teal); border-bottom: 3px solid var(--teal); padding-bottom: 0; line-height: 22px; margin-bottom: 15px; }
  .info-col h2 em { font-style: normal; color: var(--red); }
  .info-col p { font-size: 8.8px; line-height: 11.3px; color: var(--grey); padding: 0 2px; margin-bottom: 11px; }
  .why { left: 199px; }
  .says { left: 399px; }
  .news { left: 594px; }
  .benefits { list-style: none; padding-left: 2px; }
  .benefits li { display: flex; align-items: center; gap: 5px; font-size: 8.5px; font-weight: 600; height: 16px; }
  .quote-mark { font-size: 50px; line-height: 40px; color: var(--red); font-family: Georgia, serif; font-weight: 700; height: 46px; padding-left: 0; }
  .attribution { font-size: 8.5px; color: var(--grey); font-weight: 600; line-height: 11px; padding-left: 2px; margin-top: 12px; }
  .col-btn { top: 1029px; width: 57px; height: 22px; line-height: 22px; }

  /* footer */
  .site-footer { left: 0; top: 1063px; width: 993px; height: 137px; background: var(--black); }
  .call-band { left: 184px; top: 1px; width: 621px; height: 40px; background: var(--teal); color: var(--white); font-weight: 700; font-size: 20px; letter-spacing: 4px; text-align: center; line-height: 40px; }
  .site-footer .brand-wrap { left: 200px; top: 55px; }
  .site-footer .tagline { color: var(--footer-tag); }
  .site-footer .copyright { left: 198px; top: 100px; color: var(--white); font-size: 11.5px; }
  .social { left: 611px; top: 58px; display: flex; gap: 3px; }
  .social span { width: 26px; height: 26px; border-radius: 50%; background: var(--white); border: 2px solid #d9d9d9; display: flex; align-items: center; justify-content: center; }
  .social span i { width: 10px; height: 10px; border-radius: 50%; background: var(--black); }
  .legal { left: 641px; top: 98px; color: #a9a9a9; font-size: 11px; }
</style>
</head>
<body>

<div class="abs utility-bar">
  <div class="abs join">Join</div>
  <div class="abs sign-in">Sign In</div>
</div>

<header class="abs site-header">
  <div class="abs brand-wrap">
    <div class="brand"><span class="mark"></span><span class="name">FernQuill</span></div>
    <div class="tagline">It's your fashion brand</div>
  </div>
  <div class="abs divider"></div>
  <nav class="abs main-nav">
    <span class="new">New!</span><span>Tops</span><span>Bottoms</span><span>Dresses</span><span>Accessories</span><span>Clearance</span><span>Blog</span>
  </nav>
  <div class="abs search">
    <svg width="9" height="9" viewBox="0 0 9 9"><circle cx="3.6" cy="3.6" r="2.6" fill="none" stroke="#46c6c6" stroke-width="1.2"/><line x1="5.6" y1="5.6" x2="8.3" y2="8.3" stroke="#46c6c6" stroke-width="1.4"/></svg>
  </div>
</header>

<div class="abs backdrop" role="img" aria-label="Soft sunlit beach haze with bokeh light"></div>

<section class="abs hero" role="img" aria-label="Summer campaign photo: model in a polka-dot sundress on a sunny beach beside a hand-lettered Say Hello to Summer headline">
  <div class="abs cta">Start Shopping Now</div>
</section>
<div class="abs slider-dots"><span class="active"></span><span></span><span></span><span></span><span></span></div>

<section class="abs feature-card">
  <div class="abs photo" role="img" aria-label="Model in sunglasses and an off-shoulder white top against a painted orange backdrop"></div>
  <div class="abs ribbon"></div>
  <div class="abs ribbon-text">NEW</div>
  <div class="abs shop-bar">
    <span class="abs label">SHOP NOW</span>
    <span class="abs price">$200</span>
    <span class="abs cart-btn"><svg width="14" height="12" viewBox="0 0 14 12"><path d="M1 1h2l2 7h7l1.5-5H4" fill="none" stroke="#fff" stroke-width="1.3"/><circle cx="6" cy="10.5" r="1" fill="#fff"/><circle cx="11" cy="10.5" r="1" fill="#fff"/></svg></span>
  </div>
</section>

<section class="abs welcome">
  <h1>Welcome to FernQuill</h1>
  <p>Lorem Ipsum is simply dummy text of the printing and typesetting industry. Lorem Ipsum has been the industry's standard dummy text ever since the 1500s, when an unknown printer took a galley of type and scrambled it to make a type specimen book.</p>
  <p>It has survived not only five centuries, but also the leap into electronic typesetting, remaining essentially unchanged. It was popularised in the 1960s with the release of Letraset sheets containing Lorem Ipsum passages, and more recently with desktop publishing software like Aldus PageMaker including versions of Lorem Ipsum.</p>
  <div class="btn-dark">Read More</div>
</section>

<div class="abs tabs">
  <div class="tab active">LATEST PRODUCT</div>
  <div class="tab">FEATURED</div>
  <div class="tab">TOP SELLERS</div>
</div>
<section class="abs product-panel">
  <div class="abs product p1" role="img" aria-label="Model in a fitted lilac dress">
    <div class="abs overlay">PRODUCT NAME<br>$150<br>SHOP NOW
      <span class="abs cart-btn"><svg width="14" height="12" viewBox="0 0 14 12"><path d="M1 1h2l2 7h7l1.5-5H4" fill="none" stroke="#fff" stroke-width="1.3"/><circle cx="6" cy="10.5" r="1" fill="#fff"/><circle cx="11" cy="10.5" r="1" fill="#fff"/></svg></span>
    </div>
  </div>
  <div class="abs product p2" role="img" aria-label="Grey long-sleeve top"></div>
  <div class="abs product p3" role="img" aria-label="Model in a red blazer"></div>
  <div class="abs product p4" role="img" aria-label="Faded denim jacket"></div>
  <p class="abs blurb">Lorem Ipsum is simply dummy text of the printing and typesetting industry. Lorem Ipsum has been the industry's standard dummy text ever since the 1500s, when an unknown printer took a galley of</p>
  <div class="abs btn-dark">View All</div>
</section>

<section class="abs info-col why">
  <h2>WHY <em>US</em></h2>
  <p>Lorem Ipsum is simply dummy text of the printing and typesetting industry. Lorem Ipsum has been the</p>
  <ul class="benefits">
    <li><svg width="10" height="10" viewBox="0 0 10 10"><path d="M1 5.5l3 3L9.5 1" fill="none" stroke="#c8262c" stroke-width="2"/></svg>Shipping &amp; Returns</li>
    <li><svg width="10" height="10" viewBox="0 0 10 10"><path d="M1 5.5l3 3L9.5 1" fill="none" stroke="#c8262c" stroke-width="2"/></svg>Secure Shopping</li>
    <li><svg width="10" height="10" viewBox="0 0 10 10"><path d="M1 5.5l3 3L9.5 1" fill="none" stroke="#c8262c" stroke-width="2"/></svg>International Shipping</li>
    <li><svg width="10" height="10" viewBox="0 0 10 10"><path d="M1 5.5l3 3L9.5 1" fill="none" stroke="#c8262c" stroke-width="2"/></svg>Affiliates</li>
    <li><svg width="10" height="10" viewBox="0 0 10 10"><path d="M1 5.5l3 3L9.5 1" fill="none" stroke="#c8262c" stroke-width="2"/></svg>Group Sales</li>
  </ul>
</section>

<section class="abs info-col says">
  <h2>WHAT PEOPLE <em>SAY</em></h2>
  <div class="quote-mark">&ldquo;</div>
  <p>Lorem Ipsum is simply dummy text of the printing and typesetting industry. Lorem Ipsum has been the</p>
  <div class="attribution">Name ....<br>USA</div>
</section>
<div class="abs btn-dark col-btn" style="left:530px">View All</div>

<section class="abs info-col news">
  <h2>LATEST <em>NEWS</em></h2>
  <p>Lorem Ipsum is simply dummy text of the printing and typesetting industry. Lorem Ipsum has been the</p>
  <p>industry's standard dummy text ever since the 1500s, when an unknown printer took a galley of</p>
</section>
<div class="abs btn-dark col-btn" style="left:701px">View All</div>

<footer class="abs site-footer">
  <div class="abs call-band">Call Us Now! 03 5550 1742</div>
  <div class="abs brand-wrap">
    <div class="brand"><span class="mark"></span><span class="name">FernQuill</span></div>
    <div class="tagline">It's your fashion brand</div>
  </div>
  <div class="abs copyright">Copyright &copy; FernQuill All rights reserved.</div>
  <div class="abs social" aria-label="Social links">
    <span><i></i></span><span><i></i></span><span><i></i></span><span><i></i></span><span><i></i></span>
    <span><svg width="14" height="10" viewBox="0 0 14 10"><rect x=".5" y=".5" width="13" height="9" fill="#060304"/><path d="M1 1l6 5 6-5" fill="none" stroke="#fff" stroke-width="1.2"/></svg></span>
  </div>
  <div class="abs legal">Privacy Policy &nbsp;| &nbsp;Legal Notices</div>
</footer>

</body>
</html>
```